JAR LABEL FOR GUMMIES

I need a design of a label for jar with Gummy candies:
- label size: 21.5 cm length, 5.4 cm height with rounded angles. The size of the label is in attached.
-The label must include the name of the product BELLO'S VITAMIN D, as the second word (VITAMIN D) may be situated under the name BELLO'S or slighly down on the right.
-The shape of the gummies is hearts, so the label must include an illustration of 1 or 2 hearts.
-From the text in attached the information in green should be in the center, that is visible at the front of the label.
-The logo of the Company - RKW is also in attached and there is no need to be in front. The rest of the information of the label must be situated on the right and left side of the center part.

-A white, empty space with dimesnions around 5 cm long and 1 sm height should be left on the back, so the recycle icons will be inserted later on.
-The destination of the products is kids and adults.
-The jar is transparent with aluminium cap - gold or silver color.
We are looking for a playful of stylish design of the label. The product will be sold mostly in pharmacies, where there is huge competition, so it has to capture the attention. We would like to highlight the NO COLOURS, NATURAL FLAVOURS writing and 36 PECTING GUMMY CANDIES as well. The product will have different variations so it will be appreciated if the design is provided in few colors – if possible strong colors.

In attched I am providing:
- bar code
- logo of the company - RKW
- the dimensions of the label
- the text for the label.
- photo of the jar for the label

Target Market(s)

Kids and adults

Industry/Entity Type

NUTRACEUTICAL

Colors
00AB8E
00BBA5
67D7C9
C6EFE9
E9F9F6
FFC000
F8CF3A
FAE287
FDF2CF
FEFAEE
F0912C
F2A743
F7CA91
FBE8D2
FDF5EE
EB3D1F
EC4F4E
F09395
F8D3D4
FCEDEE
E54698
E96AAD
F1A4CE
F9D9EA
FCEFF6
A7469A
B969AE
D3A5CF
EDDBEB
F8F0F9

Requirements
Must have
• HEART DESIGN, NICE ACTIVE COLOURS

```html
<!DOCTYPE html>
<html lang="en">
<head>
<meta charset="utf-8">
<title>BELLO'S VITAMIN D – Jar Label</title>
<link href="https://fonts.googleapis.com/css2?family=Open+Sans:wght@700;800&family=Roboto+Condensed:wght@400;500&display=swap" rel="stylesheet">
<style>
  :root {
    --bg: #ffffff;
    --yellow-deep: #f2c400;
    --yellow-light: #fdf2cf;
    --red: #d7140f;
    --red-dark: #a50d0b;
    --red-bright: #eb3d1f;
    --gold-text: #ffd400;
    --white: #ffffff;
  }
  html, body {
    margin: 0;
    width: 1200px;
    height: 1200px;
    overflow: hidden;
    background: var(--bg);
  }
  .canvas {
    position: relative;
    width: 1200px;
    height: 1200px;
  }
  .label {
    position: absolute;
    left: 50px;
    top: 171px;
    width: 1100px;
    height: 858px;
  }
  .brand-name {
    font-family: "Open Sans", sans-serif;
    font-weight: 800;
    fill: var(--white);
  }
  .product-name {
    font-family: "Open Sans", sans-serif;
    font-weight: 800;
    fill: var(--gold-text);
  }
  .flavour {
    font-family: "Roboto Condensed", sans-serif;
    font-weight: 500;
    fill: var(--white);
  }
  .supplement-title {
    font-family: "Open Sans", sans-serif;
    font-weight: 700;
    fill: var(--white);
  }
  .supplement-claim {
    font-family: "Roboto Condensed", sans-serif;
    font-weight: 400;
    fill: var(--white);
  }
  .count-line {
    font-family: "Open Sans", sans-serif;
    font-weight: 700;
    fill: var(--gold-text);
  }
</style>
</head>
<body>
<main class="canvas">
  <svg class="label" viewBox="0 0 1000 780" xmlns="http://www.w3.org/2000/svg" aria-label="BELLO'S VITAMIN D gummy jar label">
    <defs>
      <radialGradient id="label-yellow" cx="0.5" cy="0.45" r="0.6">
        <stop offset="0" stop-color="var(--yellow-light)"/>
        <stop offset="1" stop-color="var(--yellow-deep)"/>
      </radialGradient>
      <radialGradient id="emblem-red" cx="0.4" cy="0.35" r="0.75">
        <stop offset="0" stop-color="var(--red-bright)"/>
        <stop offset="1" stop-color="var(--red-dark)"/>
      </radialGradient>
      <clipPath id="label-shape">
        <rect x="0" y="0" width="1000" height="780" rx="24"/>
      </clipPath>
    </defs>

    <g clip-path="url(#label-shape)">
      <rect class="label-base" x="0" y="0" width="1000" height="780" fill="url(#label-yellow)"/>
      <path class="label-red-band" d="M0 430 Q500 760 1000 430 L1000 780 L0 780 Z" fill="var(--red)"/>
    </g>

    <rect class="heart-emblem" x="245" y="100" width="480" height="520" rx="90"
          fill="url(#emblem-red)" role="img" aria-label="Glossy red heart illustration with gold outline"/>

    <text class="brand-name" x="485" y="320" font-size="80" text-anchor="middle">BELLO'S</text>
    <text class="product-name" x="485" y="398" font-size="66" text-anchor="middle">VITAMIN D</text>

    <g class="flavour-ribbon">
      <path d="M290 455 L740 432 L720 470 L760 505 L300 525 L312 490 Z" fill="var(--red-dark)"/>
      <path d="M300 455 L730 435 L735 495 L305 515 Z" fill="var(--red)"/>
      <text class="flavour" x="518" y="490" font-size="36" text-anchor="middle" transform="rotate(-2 518 490)">VANILLA LEMON FLAVOUR</text>
    </g>

    <g class="claim-badge claim-badge--left">
      <circle cx="178" cy="505" r="56" fill="var(--white)"/>
      <circle cx="178" cy="505" r="46" fill="var(--red)"/>
    </g>
    <g class="claim-badge claim-badge--right">
      <circle cx="829" cy="507" r="56" fill="var(--white)"/>
      <circle cx="829" cy="507" r="46" fill="var(--red)"/>
    </g>

    <text class="supplement-title" x="492" y="668" font-size="38" text-anchor="middle">FOOD SUPPLEMENT</text>
    <text class="supplement-claim" x="492" y="708" font-size="34" text-anchor="middle">With Natural Flavours and No Colours</text>
    <text class="count-line" x="492" y="748" font-size="29" text-anchor="middle">36 PECTIN GUMMY CANDIES</text>
  </svg>
</main>
</body>
</html>
```